Gutschein für Onlineshop DIN A Lang
Zielgruppe
Wir betreiben unter www.feldkiste-online.example einen Onlineshop für Armee- und Outdoorbekleidung sowie Ausrüstung. Für eine Paketbeilage benötigen wir einen Gutschein
Aufgabenstellung
Erstellung eines Gutscheins im DIN A Lang Format (Kuvert) mit Vorder- und Rückseite im CI der Webseite. Logo kann gerne zur Verfügung gestellt werden.
Gutscheincode, Wert und Laufzeit wird noch mitgeteilt.

```html
<!DOCTYPE html>
<html lang="de">
<head>
<meta charset="utf-8">
<title>Gutschein Feldkiste</title>
<link href="https://fonts.googleapis.com/css2?family=Arimo:wght@400;700&display=swap" rel="stylesheet">
<style>
  :root {
    --olive-dark: #46463a;
    --olive: #5a5b45;
    --khaki: #c9c78c;
    --paper: #ffffff;
    --text-dark: #3e3f30;
    --sky-top: #7e9dc4;
    --sky-mid: #b9cbe0;
    --snow: #eef2f7;
  }
  html, body {
    margin: 0;
    padding: 0;
    width: 988px;
    height: 1200px;
    overflow: hidden;
    background: var(--paper);
    font-family: "Arimo", Arial, sans-serif;
  }
  .canvas { position: relative; width: 988px; height: 1200px; }
  .voucher { position: absolute; left: 82px; width: 844px; overflow: hidden; }
  .voucher--front { top: 74px; height: 416px; }
  .voucher--back { top: 558px; height: 418px; }
  .top-band { position: absolute; left: 0; top: 0; width: 100%; height: 44px; background: var(--olive-dark); }
  .masthead {
    position: absolute; left: 0; top: 44px; width: 100%; height: 110px;
    display: flex; align-items: center; border-bottom: 4px solid var(--olive-dark);
    box-sizing: border-box;
  }
  .brand {
    margin-left: 48px; width: 200px; display: flex; align-items: center; gap: 8px;
    font-weight: 700; font-size: 26px; color: var(--olive); letter-spacing: -0.5px;
  }
  .brand__mark { width: 14px; height: 14px; background: var(--khaki); }
  .title {
    margin-left: 20px; font-weight: 700; font-size: 96px; line-height: 1;
    color: var(--olive-dark); letter-spacing: 1px;
  }
  .landscape {
    position: absolute; left: 0; width: 100%; overflow: hidden;
    background: linear-gradient(180deg, var(--sky-top) 0%, var(--sky-mid) 45%, var(--snow) 80%, #d7dfe9 100%);
  }
  .voucher--front .landscape { top: 166px; height: 204px; }
  .voucher--back .landscape { top: 156px; height: 212px; }
  .value-disc {
    position: absolute; left: 542px; top: -30px; width: 272px; height: 272px;
    border-radius: 50%; background: var(--khaki); opacity: 0.85;
    display: flex; align-items: center; justify-content: center;
    font-weight: 700; font-size: 84px; color: var(--olive-dark);
  }
  .info-disc {
    position: absolute; left: -74px; top: -126px; width: 500px; height: 500px;
    border-radius: 50%; background: rgba(255,255,255,0.55);
  }
  .details { position: absolute; left: 58px; top: 14px; color: var(--text-dark); }
  .details p { margin: 0; font-weight: 700; font-size: 24px; line-height: 27px; }
  .issuer { margin-top: 24px; font-size: 12px; line-height: 14px; font-weight: 400; }
  .issuer div { margin: 0; }
  .url-band {
    position: absolute; left: 0; bottom: 0; width: 100%; height: 46px;
    background: var(--olive-dark); color: var(--paper);
    font-weight: 700; font-size: 29px; line-height: 46px; box-sizing: border-box;
  }
  .voucher--front .url-band { padding-left: 54px; }
  .voucher--back .url-band { text-align: right; padding-right: 62px; }
</style>
</head>
<body>
<div class="canvas">

  <section class="voucher voucher--front">
    <div class="top-band"></div>
    <header class="masthead">
      <div class="brand"><span class="brand__mark"></span>FELDKISTE</div>
      <h1 class="title">GUTSCHEIN</h1>
    </header>
    <div class="landscape" role="img" aria-label="Verschneites Hochgebirgspanorama unter blauem Himmel">
      <div class="value-disc">25,-</div>
    </div>
    <div class="url-band">www.feldkiste-online.example</div>
  </section>

  <section class="voucher voucher--back">
    <div class="top-band"></div>
    <header class="masthead">
      <div class="brand"><span class="brand__mark"></span>FELDKISTE</div>
      <h1 class="title">GUTSCHEIN</h1>
    </header>
    <div class="landscape" role="img" aria-label="Verschneites Hochgebirgspanorama unter blauem Himmel">
      <div class="info-disc"></div>
      <div class="details">
        <p>Wert: fünfundzwanzig Euro</p>
        <p>Gültig bis: 01.01.2015</p>
        <p>Gutscheinnummer: 0123456789</p>
        <div class="issuer">
          <div>Nordlicht Handels GmbH</div>
          <div>Division Feldkiste</div>
          <div>Am Lindenhof 12-14</div>
          <div>73400 Musterhausen</div>
        </div>
      </div>
    </div>
    <div class="url-band">www.feldkiste-online.example</div>
  </section>

</div>
</body>
</html>
```